Lumora Pathway Advisory - Business card design needed

I wish to get business cards designed so that it follows my website design ... http://www.lumora-pathway.org
I need logos for QUVEX 7 and KT Summit Associate for myself which I have uploaded the files.
I wish my qualifications PhD PMP FAICD to be smaller print than my name.
Regards
Leopold
Industry/Entity Type
Business
Contact Information for Business Card
Lumora Pathway Advisory
Dr Leopold Marsh PhD PMP FAICD
Director
PO Box 418 Kelvendale NSW 2093 AUSTRALIA
T:+61 2 9352 6710 M:+61 437 918000 F: +61 2 9368 2000
Email: leopold.marsh@lumora-pathway.org
Website: http://www.lumora-pathway.org

```html
<!DOCTYPE html>
<html lang="en">
<head>
<meta charset="utf-8">
<title>Lumora Pathway Advisory – Business Card</title>
<link rel="stylesheet" href="https://fonts.googleapis.com/css2?family=Open+Sans:wght@400;600;700&display=swap">
<style>
  :root {
    --stage: #1b1b1b;
    --band: #6b6766;
    --frame: #2f2f2f;
    --card-deep: #061645;
    --card-mid: #0c2463;
    --card-glow: #14307a;
    --arc: rgba(120, 150, 210, 0.28);
    --brand-text: #b9c1d6;
    --white: #ffffff;
    --muted: #a9b3cc;
    --contact: #dfe5f2;
    --icon: #5f8fd8;
    --rule: rgba(150, 170, 215, 0.45);
    --badge-green: #2f8f7a;
    --badge-blue: #1a9ad6;
  }
  * { margin: 0; padding: 0; box-sizing: border-box; }
  html, body {
    width: 1200px; height: 900px; overflow: hidden;
    background: var(--stage);
    font-family: "Open Sans", Arial, sans-serif;
  }
  .stage { position: relative; width: 1200px; height: 900px; }
  .stage__band {
    position: absolute; left: 0; top: 320px; width: 1200px; height: 260px;
    background: var(--band);
  }
  .stage__frame {
    position: absolute; border: 2px solid var(--frame);
  }
  .stage__frame--outer { left: 25px; top: 83px; width: 1150px; height: 732px; border-radius: 8px; }
  .stage__frame--inner { left: 102px; top: 182px; width: 983px; height: 570px; }

  .card {
    position: absolute; width: 595px; height: 331px; overflow: hidden;
    background:
      radial-gradient(ellipse 90% 60% at 60% 100%, var(--card-glow) 0%, transparent 70%),
      linear-gradient(180deg, var(--card-deep) 0%, var(--card-mid) 100%);
    box-shadow: 4px 5px 8px rgba(0,0,0,0.55);
  }
  .card--front { left: 126px; top: 92px; }
  .card--back { left: 470px; top: 470px; }

  .card__arc { position: absolute; inset: 0; }
  .card__texture {
    position: absolute; left: 0; right: 0; bottom: 0; height: 60%;
    background: linear-gradient(180deg, transparent 0%, rgba(40, 70, 150, 0.25) 100%);
  }

  .brand-art {
    position: absolute; width: 64px; height: 72px; border-radius: 40% 45% 40% 40%;
    background: radial-gradient(circle at 50% 45%, #c7d6ee 0%, #6f8fc6 45%, rgba(20,48,122,0) 75%);
  }
  .brand-name {
    position: absolute; color: var(--brand-text);
    font-weight: 600; font-size: 18px; line-height: 24px;
  }

  .card--front .brand-art { left: 33px; top: 20px; }
  .card--front .brand-name { left: 111px; top: 33px; }

  .holder { position: absolute; left: 41px; top: 173px; color: var(--white); }
  .holder__name { font-size: 20px; font-weight: 700; line-height: 24px; }
  .holder__quals { font-size: 11px; font-weight: 600; color: var(--muted); margin-left: 2px; }
  .holder__role { font-size: 13px; font-weight: 700; line-height: 16px; }

  .contact-rule {
    position: absolute; left: 39px; top: 222px; width: 520px; height: 1px; background: var(--rule);
  }
  .contact-divider {
    position: absolute; left: 205px; top: 225px; width: 1px; height: 77px; background: var(--rule);
  }
  .contact-list { position: absolute; list-style: none; }
  .contact-list--phones { left: 44px; top: 240px; }
  .contact-list--online { left: 250px; top: 240px; }
  .contact-list li {
    display: flex; align-items: center; gap: 8px;
    height: 19.5px; font-size: 12px; color: var(--contact);
  }
  .contact-list svg { width: 12px; height: 12px; fill: var(--icon); flex: none; }

  .card--back .brand-name { right: 32px; top: 21px; text-align: left; }
  .card--back .brand-art { left: 498px; top: 58px; }

  .cert-badge { position: absolute; left: 22px; top: 168px; width: 180px; height: 52px; }
  .partner-badge {
    position: absolute; left: 22px; top: 249px; width: 122px; height: 43px;
    background: var(--badge-blue); border-radius: 2px;
  }
</style>
</head>
<body>
<div class="stage">
  <div class="stage__band"></div>
  <div class="stage__frame stage__frame--outer"></div>
  <div class="stage__frame stage__frame--inner"></div>

  <section class="card card--front">
    <div class="card__texture"></div>
    <svg class="card__arc" viewBox="0 0 595 331" aria-hidden="true">
      <path d="M0 165 Q 260 40 595 92" fill="none" stroke="var(--arc)" stroke-width="10"/>
      <path d="M0 175 Q 260 55 595 100" fill="none" stroke="rgba(120,150,210,0.12)" stroke-width="4"/>
    </svg>
    <div class="brand-art" role="img" aria-label="Brand illustration: head in profile with technology imagery"></div>
    <div class="brand-name">Lumora Pathway<br>Advisory</div>

    <div class="holder">
      <div class="holder__name">Dr. Leopold Marsh<span class="holder__quals">PhD PMP FAICD</span></div>
      <div class="holder__role">Director</div>
    </div>

    <div class="contact-rule"></div>
    <div class="contact-divider"></div>

    <ul class="contact-list contact-list--phones">
      <li><svg viewBox="0 0 24 24"><path d="M6.6 10.8a15 15 0 0 0 6.6 6.6l2.2-2.2a1 1 0 0 1 1-.25 11.4 11.4 0 0 0 3.6.57 1 1 0 0 1 1 1V20a1 1 0 0 1-1 1A17 17 0 0 1 3 4a1 1 0 0 1 1-1h3.5a1 1 0 0 1 1 1c0 1.25.2 2.45.57 3.6a1 1 0 0 1-.25 1z"/></svg>+61-437-918000</li>
      <li><svg viewBox="0 0 24 24"><rect x="3" y="2" width="6" height="20" rx="1"/><rect x="10" y="5" width="11" height="17" rx="1"/><rect x="12" y="8" width="7" height="3" fill="#0c2463"/></svg>+61-2-9352-6710</li>
      <li><svg viewBox="0 0 24 24"><rect x="6" y="2" width="12" height="6"/><rect x="2" y="9" width="20" height="9" rx="1"/><rect x="6" y="15" width="12" height="7"/></svg>+61-2-9368-2000</li>
    </ul>

    <ul class="contact-list contact-list--online">
      <li><svg viewBox="0 0 24 24"><path d="M2 5h20v14H2z"/><path d="M2 5l10 8 10-8" fill="none" stroke="#0c2463" stroke-width="2"/></svg>leopold.marsh@lumora-pathway.org</li>
      <li><svg viewBox="0 0 24 24"><circle cx="12" cy="12" r="10"/><path d="M2 12h20M12 2c3 3 3 17 0 20M12 2c-3 3-3 17 0 20" fill="none" stroke="#0c2463" stroke-width="1.5"/></svg>www.lumora-pathway.org</li>
      <li><svg viewBox="0 0 24 24"><path d="M12 2a7 7 0 0 0-7 7c0 5 7 13 7 13s7-8 7-13a7 7 0 0 0-7-7zm0 9.5A2.5 2.5 0 1 1 12 6.5a2.5 2.5 0 0 1 0 5z"/></svg>PO Box 418 Kelvendale NSW 2093 AUSTRALIA</li>
    </ul>
  </section>

  <section class="card card--back">
    <div class="card__texture"></div>
    <svg class="card__arc" viewBox="0 0 595 331" aria-hidden="true">
      <path d="M0 75 Q 260 40 595 155" fill="none" stroke="var(--arc)" stroke-width="10"/>
      <path d="M0 85 Q 260 52 595 165" fill="none" stroke="rgba(120,150,210,0.12)" stroke-width="4"/>
    </svg>
    <div class="brand-name">Lumora Pathway<br>Advisory</div>
    <div class="brand-art" role="img" aria-label="Brand illustration: head in profile with technology imagery"></div>

    <svg class="cert-badge" viewBox="0 0 180 52" role="img" aria-label="QUVEX 7 certification badge">
      <circle cx="24" cy="26" r="22" fill="var(--badge-green)"/>
      <rect x="54" y="24" width="124" height="2" fill="var(--badge-green)"/>
    </svg>
    <div class="partner-badge" role="img" aria-label="KT Summit Associate partner badge"></div>
  </section>
</div>
</body>
</html>
```